Aromatherapy product co needs a pre-set label stickers for essential oil bottle

We need a label sticker for all our essential oils range, leave the blank area for us to key in the contents, such as essential oil name, expiry date, description, weight, precaution and company contact details.
The label should express the nature, organic, colourful of the products. Especially essential oil is related to plants, leaf and flower. Therefore, we hope the design can close to nature and more colours and high quality.
The label size is 35 mm x 90 mm in horizon way. Just nice to wrap the whole bottle. Can divide the label into 2 or 3 portion. We would like to put in our logo into the label. You can see our present lable design in our website : http://quillmora-living.com/product-category/aromatherapy/organic-pure-essential-oils/

Target Market(s)

We sell only organic essential oils, our target market is to end user who appreciate of high quality of the products and love the nature.

Industry/Entity Type

Health And Wellness

Font styles to use
Sans Serif

Requirements
Must have
• Our die cut label is in white colour. We can accept white base or light olive green base as long the label look outstanding.
• We prefer have frame for our label, divide it into 2 or 3 portion such as name of the product, botanical name, weight at the centre, other information at both side.
• We can accept full colour design as we now have colour label printer.
Nice to have
• Plants, leaf or flower either in real or graphic type, the label must look grand and high quality. And expression of nature and quality products.
Should not have
• colours that not represent nature such as black colour.

```html
<!DOCTYPE html>
<html lang="en">
<head>
<meta charset="utf-8">
<title>Quillmora Essential Oil Labels</title>
<link rel="stylesheet" href="https://fonts.googleapis.com/css2?family=Bebas+Neue&family=Roboto+Condensed:wght@400;700&display=swap">
<style>
  :root {
    --page: #ffffff;
    --frame: #8a8a8a;
    --white: #ffffff;
    --brand: #c9742f;

    --citronella-ink: #f0a020;
    --citronella-band: #f0a823;
    --citronella-top: #fff1c4;
    --citronella-low-a: #fee99a;
    --citronella-low-b: #f9d518;

    --eucalyptus-ink: #1a6133;
    --eucalyptus-band: #166133;
    --eucalyptus-top: #e2eecf;
    --eucalyptus-low-a: #bcdf96;
    --eucalyptus-low-b: #8cc63f;

    --geranium-ink: #d0223e;
    --geranium-band: #d3223f;
    --geranium-top: #fbdfe9;
    --geranium-low-a: #f9d0df;
    --geranium-low-b: #f29fc0;

    --teatree-ink: #0f7a86;
    --teatree-band: #0f7a86;
    --teatree-top: #dbf0f7;
    --teatree-low-a: #b0e2ef;
    --teatree-low-b: #6bc8df;
  }
  * { box-sizing: border-box; margin: 0; padding: 0; }
  html, body {
    width: 886px; height: 1200px; overflow: hidden;
    background: var(--page);
    font-family: "Roboto Condensed", Arial, sans-serif;
  }
  .sheet { position: relative; width: 886px; height: 1200px; }

  .label {
    position: absolute; left: 205px; width: 468px; height: 183px;
    border: 1px solid var(--frame);
    overflow: hidden;
    background: linear-gradient(to bottom, var(--white) 0%, var(--top) 96px);
  }
  .label--citronella { top: 207px; --ink: var(--citronella-ink); --band: var(--citronella-band); --top: var(--citronella-top); --low-a: var(--citronella-low-a); --low-b: var(--citronella-low-b); }
  .label--eucalyptus { top: 409px; --ink: var(--eucalyptus-ink); --band: var(--eucalyptus-band); --top: var(--eucalyptus-top); --low-a: var(--eucalyptus-low-a); --low-b: var(--eucalyptus-low-b); }
  .label--geranium   { top: 612px; --ink: var(--geranium-ink); --band: var(--geranium-band); --top: var(--geranium-top); --low-a: var(--geranium-low-a); --low-b: var(--geranium-low-b); }
  .label--teatree    { top: 817px; --ink: var(--teatree-ink); --band: var(--teatree-band); --top: var(--teatree-top); --low-a: var(--teatree-low-a); --low-b: var(--teatree-low-b); }

  .brand-plate {
    position: absolute; left: 188px; top: 0; width: 92px; height: 63px;
    background: var(--white);
    display: flex; align-items: center; justify-content: center;
    color: var(--brand);
  }
  .brand-name { font-size: 17px; font-weight: 400; letter-spacing: 0.5px; line-height: 1; margin-top: 6px; }

  .claim {
    position: absolute; left: 6px; top: 34px; width: 110px;
    color: var(--ink); font-size: 8.3px; line-height: 10.2px;
  }
  .claim strong { font-weight: 700; font-size: 8.6px; }

  .name-band {
    position: absolute; left: 0; top: 96px; width: 100%; height: 38px;
    background: var(--band); color: var(--white);
  }
  .site {
    position: absolute; left: 6px; top: 13px;
    font-size: 8.4px; font-weight: 700;
  }
  .oil-name {
    position: absolute; left: 0; right: 0; top: 5px; text-align: center;
    font-family: "Bebas Neue", "Arial Narrow", sans-serif;
    font-weight: 400;
    font-size: 18px; line-height: 19px; letter-spacing: 0.3px;
  }
  .oil-meta {
    position: absolute; left: 0; right: 0; top: 24px; text-align: center;
    font-size: 6px; font-weight: 700; letter-spacing: 0.1px;
  }

  .base-strip {
    position: absolute; left: 0; top: 134px; width: 100%; height: 49px;
    background: linear-gradient(to bottom, var(--low-a), var(--low-b));
  }
</style>
</head>
<body>
<main class="sheet">

  <section class="label label--citronella">
    <div class="brand-plate"><span class="brand-name">QUILLMORA</span></div>
    <p class="claim"><strong>100% pure essential oil</strong><br>therapeutic grade according<br>to international standards<br>and suitable for all aroma-<br>therapy applications</p>
    <div class="name-band">
      <span class="site">www.quillmora-living.com</span>
      <h2 class="oil-name">Citronella</h2>
      <p class="oil-meta">NEPAL / ORGANIC&nbsp; NET WT: 15 ML</p>
    </div>
    <div class="base-strip"></div>
  </section>

  <section class="label label--eucalyptus">
    <div class="brand-plate"><span class="brand-name">QUILLMORA</span></div>
    <p class="claim"><strong>100% pure essential oil</strong><br>therapeutic grade according<br>to international standards<br>and suitable for all aroma-<br>therapy applications</p>
    <div class="name-band">
      <span class="site">www.quillmora-living.com</span>
      <h2 class="oil-name">Eucalyptus</h2>
      <p class="oil-meta">USA / ORGANIC&nbsp; NET WT: 15 ML</p>
    </div>
    <div class="base-strip"></div>
  </section>

  <section class="label label--geranium">
    <div class="brand-plate"><span class="brand-name">QUILLMORA</span></div>
    <p class="claim"><strong>100% pure essential oil</strong><br>therapeutic grade according<br>to international standards<br>and suitable for all aroma-<br>therapy applications</p>
    <div class="name-band">
      <span class="site">www.quillmora-living.com</span>
      <h2 class="oil-name">Geranium Rose</h2>
      <p class="oil-meta">EGYPT / ORGANIC&nbsp; NET WT: 15 ML</p>
    </div>
    <div class="base-strip"></div>
  </section>

  <section class="label label--teatree">
    <div class="brand-plate"><span class="brand-name">QUILLMORA</span></div>
    <p class="claim"><strong>100% pure essential oil</strong><br>therapeutic grade according<br>to international standards<br>and suitable for all aroma-<br>therapy applications</p>
    <div class="name-band">
      <span class="site">www.quillmora-living.com</span>
      <h2 class="oil-name">Tea Tree</h2>
      <p class="oil-meta">AUSTRALIA / ORGANIC NET WT: 15 ML</p>
    </div>
    <div class="base-strip"></div>
  </section>

</main>
</body>
</html>
```